Crispy Jerky Packaging for KO.MU

We need packaging for for our hand-crafted crispy beef jerky. We are launching a new product that is like eating a potato chip, but made of beef/pork. We would like to have a window for people to be able to see our product. It is a new type of jerky, so we need the audience to be able to see that they are getting value for what they are paying for. Where a traditional 1oz portion of jerky would have 10-11g protein, ours has 20g of protein. It is also easy on the jaw because there is no tearing off of the jerky, it eats just like a chip
Updates

Target Market(s)

Beer lovers/ health-conscious/ millenials

Industry/Entity Type

Product

Font styles to use
Other font styles liked:
• be creative

Colors
fbed22
9bcb3b
85cae6

Requirements
Must have
• Yellow packaging base
• 20g Protein per serving
• Made in Hawaii
Nice to have
• Would prefer the current font we have for the company name, KO.MU
Should not have
• cows

```html
<!DOCTYPE html>
<html lang="en">
<head>
<meta charset="utf-8">
<title>KO.MU Crispy Beef Jerky Pouch</title>
<link rel="stylesheet" href="https://fonts.googleapis.com/css2?family=Kreon:wght@400;600&family=Quicksand:wght@500;600&family=Delius&display=swap">
<style>
  :root {
    --backdrop: #eeece6;
    --pouch: #e3e86b;
    --pouch-seal: #d6dc55;
    --pouch-edge: #c9cf48;
    --label: #231f20;
    --green: #9bcb3b;
    --blue: #85cae6;
    --white: #ffffff;
    --faint: #3a3738;
  }
  * { margin: 0; padding: 0; box-sizing: border-box; }
  html, body { width: 800px; height: 1200px; overflow: hidden; }
  body { background: var(--backdrop); position: relative; font-family: "Quicksand", sans-serif; }

  .pouch { position: absolute; left: 90px; top: 125px; width: 615px; height: 965px; }
  .pouch svg { display: block; }

  .label {
    position: absolute; left: 190px; top: 411px; width: 398px; height: 542px;
    background: var(--label); color: var(--white); overflow: hidden;
  }
  .label-watermark {
    position: absolute; left: 190px; top: 250px; transform: rotate(-90deg); transform-origin: left top;
    font-family: "Kreon", serif; font-weight: 600; font-size: 150px; color: var(--faint);
    white-space: nowrap; line-height: 1;
  }
  .brand-name {
    position: absolute; left: 82px; top: 215px; transform: translate(-50%, -50%) rotate(-90deg);
    font-family: "Kreon", serif; font-weight: 600; font-size: 74px; color: var(--blue);
    white-space: nowrap; line-height: 1; letter-spacing: 2px;
  }
  .divider { position: absolute; left: 162px; top: 41px; width: 1px; height: 311px; background: #8a8889; }

  .tagline { position: absolute; left: 175px; top: 68px; font-size: 14px; color: var(--blue); font-weight: 500; }
  .product-name {
    position: absolute; left: 174px; top: 95px; font-family: "Kreon", serif; font-weight: 400;
    font-size: 52px; line-height: 46px; color: var(--green); letter-spacing: 1px;
  }
  .origin-pill {
    position: absolute; left: 176px; top: 201px; width: 158px; height: 24px;
    background: var(--blue); color: var(--label); border-radius: 6px;
    font-size: 18px; font-weight: 500; line-height: 24px; text-align: center;
  }
  .benefits { position: absolute; left: 176px; top: 242px; list-style: none; font-size: 17px; font-weight: 500; line-height: 21px; }
  .benefits li::before { content: ""; display: inline-block; width: 10px; height: 8px; background: var(--white); margin-right: 8px; vertical-align: 2px; }
  .net-weight { position: absolute; left: 176px; top: 336px; font-family: "Kreon", serif; font-size: 12px; color: var(--green); }
  .net-weight strong { font-weight: 600; }

  .allergen { position: absolute; left: 163px; top: 411px; font-family: "Delius", cursive; font-size: 11px; }
  .info-box {
    position: absolute; left: 25px; top: 425px; width: 357px; height: 99px;
    border: 1px solid var(--green); border-radius: 5px;
  }
  .ingredients {
    position: absolute; left: -1px; top: -1px; width: 134px; height: 99px;
    background: var(--green); border-radius: 5px 0 0 5px; color: #3b3f2c;
    font-family: "Delius", cursive; font-size: 12px; padding: 4px 14px;
  }
  .contact { position: absolute; left: 140px; top: 7px; font-family: "Delius", cursive; font-size: 12px; line-height: 16px; }
  .contact strong { font-weight: 700; }
  .contact .web { font-family: "Quicksand", sans-serif; font-size: 18px; line-height: 22px; margin-top: 1px; }
  .social { position: absolute; left: 140px; top: 76px; display: flex; gap: 10px; align-items: center; font-family: "Quicksand", sans-serif; font-size: 10px; color: var(--green); }
  .social .dot { width: 11px; height: 11px; border-radius: 50%; background: var(--green); display: inline-block; margin-right: 4px; vertical-align: -1px; }
  .storage { position: absolute; right: 20px; top: 529px; font-size: 6px; color: var(--blue); letter-spacing: 0.3px; }
</style>
</head>
<body>
  <div class="pouch" role="img" aria-label="Translucent yellow stand-up pouch with window showing the crispy jerky">
    <svg width="615" height="965" viewBox="0 0 615 965">
      <rect x="0" y="0" width="615" height="965" rx="6" fill="var(--pouch)"/>
      <rect x="48" y="112" width="520" height="810" fill="var(--pouch-seal)" opacity="0.55"/>
      <rect x="48" y="112" width="520" height="810" fill="none" stroke="var(--pouch-edge)" stroke-width="1"/>
      <rect x="18" y="18" width="579" height="929" fill="none" stroke="var(--pouch-edge)" stroke-width="1" opacity="0.6"/>
      <path d="M247 80 h35 a10 10 0 0 1 10 -10 h30 a10 10 0 0 1 10 10 h35 a12 12 0 0 1 0 24 h-120 a12 12 0 0 1 0 -24z" fill="var(--backdrop)" stroke="var(--pouch-edge)"/>
    </svg>
  </div>

  <section class="label">
    <div class="label-watermark" aria-hidden="true">KO.MU</div>
    <div class="brand-name">KO.MU</div>
    <div class="divider"></div>

    <p class="tagline">Quality Handmade Crispy</p>
    <h1 class="product-name">BEEF<br>JERKY</h1>
    <div class="origin-pill">Made in Hawaii</div>
    <ul class="benefits">
      <li>20g protein per Serving</li>
      <li>Low in Fat &amp; Carbs</li>
    </ul>
    <p class="net-weight">NET WT <strong>1.25</strong> oz <strong>(35g)</strong></p>

    <p class="allergen"><sup>*</sup>May contain soybean and wheat</p>
    <div class="info-box">
      <div class="ingredients">Ingredients:</div>
      <address class="contact" style="font-style:normal">
        <strong>2150</strong> Palm Lane , Hilo,<br>
        Hawaii <strong>96720</strong><br>
        Ph:<strong>808-555-0142</strong>
        <div class="web">www.komusnacks.com</div>
      </address>
      <div class="social"><span><span class="dot"></span>komusnacks</span></div>
    </div>
    <p class="storage">STORE IN ROOM TEMPERATURE</p>
  </section>
</body>
</html>
```